Redesign Of Current Landing Page

I need to redesign this landing page https://www.bluewillowpromos.example/?page=landing&landing=23 (Please do not opt in because when you do it will show you the home page. Please clear your cookies before going to this url above to view the 1 page landing page.)

Please use my updated website as a reference for colors and logo.
http://sitecraftorly.example/dh/bwpg/index.html

I would like the call to action to be a button that opens into a lead form...

Button would be "Download Samples"

Target Market(s)

small business owners

Industry/Entity Type

Marketing

Number of Pages Required

1 page

Colors

Designer to choose colors to be used in the design.

Requirements
Must have
• must be full responsive on all devices
Nice to have
• must have a legitimate professional apeal to it
Should not have
• open

```html
<!DOCTYPE html>
<html lang="en">
<head>
<meta charset="utf-8">
<title>Blue Willow Promos – Attract More Customers</title>
<link href="https://fonts.googleapis.com/css2?family=Montserrat:wght@500;600;700;800&family=Open+Sans:wght@400;600;700&display=swap" rel="stylesheet">
<style>
:root{
  --blue:#0a72c2;
  --blue-dark:#075a9c;
  --sky:#e0f0fa;
  --orange:#f0612a;
  --ink:#2f2f2f;
  --muted:#6c6c6c;
  --line:#d9d9d9;
  --grey:#ececec;
  --white:#ffffff;
}
*{box-sizing:border-box;margin:0;padding:0}
html,body{width:1200px;height:2761px;overflow:hidden}
body{position:relative;font-family:"Open Sans",Arial,sans-serif;color:var(--ink);background:var(--white)}
.abs{position:absolute}
.heading{font-family:"Montserrat",Arial,sans-serif}

/* header */
.site-header{left:0;top:0;width:1200px;height:86px;background:var(--white)}
.brand{left:160px;top:26px;display:flex;align-items:center;gap:10px}
.brand-mark{width:30px;height:30px;background:var(--blue);border-radius:4px}
.brand-name{font-family:"Montserrat",sans-serif;font-weight:700;font-size:19px;color:var(--blue);letter-spacing:.5px}
.hours{left:830px;top:16px;text-align:center;color:var(--blue);font-family:"Montserrat",sans-serif;font-weight:800;font-size:34px;line-height:32px}
.hours small{display:block;font-size:10px;letter-spacing:2px;font-weight:600}
.hours-divider{left:888px;top:18px;width:1px;height:50px;background:var(--line)}
.phones{left:905px;top:16px;font-family:"Montserrat",sans-serif;font-weight:700;font-size:14px;color:var(--blue);line-height:29px}
.phones div{display:flex;align-items:center;gap:10px}

/* hero */
.hero{left:0;top:86px;width:1200px;height:466px;background:var(--sky)}
.hero-art{left:556px;top:78px;width:510px;height:502px;background:linear-gradient(135deg,#1b4f8f 0%,#3a8fd0 35%,#1e6b3a 60%,#7a2c8a 100%);clip-path:polygon(14% 0,100% 14%,96% 100%,8% 100%,0 62%)}
.hero-title{left:160px;top:152px;font-weight:800;font-size:46px;line-height:56px;color:var(--blue);letter-spacing:.3px;white-space:nowrap;z-index:2}
.hero-sub{left:160px;top:280px;font-size:22px;line-height:28px;color:var(--blue);z-index:2}
.btn{display:flex;align-items:center;justify-content:center;gap:12px;background:var(--blue);color:var(--white);font-family:"Montserrat",sans-serif;font-weight:600;font-size:17px;border-radius:2px}
.hero-btn{left:160px;top:378px;width:264px;height:60px}

/* about */
.about{left:0;top:552px;width:1200px;height:778px;background:linear-gradient(#ffffff,#f4f4f4)}
.imagine{left:160px;top:700px;font-weight:800;font-size:36px;color:var(--blue);white-space:nowrap}
.imagine span{color:#eef1f4}
.copy{width:410px;font-size:10.5px;line-height:17px;color:#444}
.copy b{font-weight:700;color:#222}
.copy p{margin-bottom:16px}
.copy1{left:160px;top:772px}
.rule{left:290px;top:993px;width:200px;height:1px;background:var(--line)}
.how{left:160px;top:1026px;font-weight:800;font-size:35px;color:var(--orange)}
.copy2{left:160px;top:1100px}
.why-title{left:690px;top:712px;width:380px;text-align:center;font-weight:700;font-size:18px;color:#444;white-space:nowrap}
.why-underline{left:842px;top:752px;width:76px;height:2px;background:var(--blue)}
.why-axis{left:879px;top:790px;width:1px;height:440px;background:var(--line)}
.dot{width:8px;height:8px;border-radius:50%;background:var(--orange)}
.benefit{width:170px;text-align:center;font-size:11px;line-height:18px;color:#333}
.benefit svg{display:block;margin:0 auto 16px}

/* lead */
.lead{left:0;top:1330px;width:1200px;height:598px;background:linear-gradient(#efefef,#e2e2e2)}
.card{background:var(--white);border-radius:4px;box-shadow:0 2px 6px rgba(0,0,0,.06)}
.form-card{left:160px;top:1415px;width:436px;height:372px}
.form-title{left:193px;top:1452px;width:400px;font-size:11.5px;color:#555;line-height:21px}
.form-title strong{font-family:"Montserrat",sans-serif;font-weight:800;font-size:30px;color:var(--blue);margin-right:6px}
.label{font-size:11.5px;font-weight:600;color:#222}
.field{height:40px;border:1px solid #c9dff0;border-radius:3px;font-size:12px;color:#aaa;padding:11px 12px}
.mandatory{left:480px;top:1697px;font-size:10px;color:#d33}
.form-btn{left:255px;top:1756px;width:248px;height:60px}
.testi-card{left:700px;top:1418px;width:346px;height:400px}
.testi-title{left:700px;top:1448px;width:346px;text-align:center;font-family:"Montserrat",sans-serif;font-weight:700;font-size:18px;color:var(--blue)}
.quote-mark{left:724px;top:1484px;font-family:"Montserrat",sans-serif;font-weight:800;font-size:32px;color:#999}
.testi-text{left:748px;top:1500px;width:264px;font-size:12px;line-height:22px;color:#333}
.testi-name{left:850px;top:1756px;width:158px;text-align:right;font-weight:700;font-size:13px;color:var(--blue)}
.testi-place{left:850px;top:1776px;width:158px;text-align:right;font-size:10.5px;color:#777}

/* clients */
.clients-title{left:0;top:1988px;width:1200px;text-align:center;font-weight:800;font-size:35px;color:var(--blue)}
.client-row{left:76px;top:2084px;width:1048px;display:flex;gap:52px}
.client{width:168px;height:72px;border:1px solid #e2e2e2;display:flex;align-items:center;justify-content:center;font-family:"Open Sans",sans-serif;font-weight:600;font-size:18px;color:#8a8a8a;white-space:nowrap}
.chev{top:2106px}

/* footer */
.site-footer{left:0;top:2240px;width:1200px;height:448px;background:var(--grey)}
.f-head{font-family:"Montserrat",sans-serif;font-weight:700;font-size:14px;color:#333}
.f-bar{width:38px;height:2px;background:var(--blue)}
.f-text{font-size:11.5px;line-height:20px;color:#333}
.f-about{left:160px;top:2364px;width:205px;font-size:10px;line-height:16px;color:#333}
.f-links{font-size:11px;line-height:22px;color:#333}
.social{left:160px;top:2504px;display:flex;gap:12px}
.social i{display:block;width:32px;height:32px;border-radius:50%}
.contact-row{display:flex;gap:12px}
.f-input{width:214px;height:42px;background:var(--white);border:1px solid #dcdcdc;font-size:11px;color:#888;padding:12px}
.submit{left:826px;top:2588px;width:118px;height:40px;font-size:16px}
.copyright{left:0;top:2688px;width:1200px;height:73px;background:var(--blue);color:var(--white);font-weight:700;font-size:12px;display:flex;align-items:center;justify-content:center}
</style>
</head>
<body>

<header class="site-header abs">
  <div class="brand abs"><span class="brand-mark"></span><span class="brand-name">BLUE WILLOW PROMOS</span></div>
  <div class="hours abs">24<small>HOURS</small></div>
  <div class="hours-divider abs"></div>
  <div class="phones abs">
    <div><svg width="22" height="14" viewBox="0 0 22 14"><rect width="22" height="14" fill="#c8ced6"/><rect y="0" width="22" height="2" fill="#d64545"/><rect y="4" width="22" height="2" fill="#d64545"/><rect y="8" width="22" height="2" fill="#d64545"/><rect width="9" height="7" fill="#2d4e8a"/></svg>555-014-2287</div>
    <div><svg width="22" height="16" viewBox="0 0 22 16"><circle cx="11" cy="8" r="7" fill="#3ba3dc"/><path d="M6 6q3-3 6 0t5 1" stroke="#7fc470" stroke-width="2" fill="none"/></svg>1-800-555-0199</div>
  </div>
</header>

<section class="hero abs"></section>
<div class="hero-art abs" role="img" aria-label="Fanned stack of sample incentive certificates: cash back reward, hotel stay, cruise, music player and city getaway"></div>
<h1 class="hero-title heading abs">ATTRACT MORE<br>CUSTOMERS</h1>
<p class="hero-sub abs">who spend more money with your<br>busines moreo ften!</p>
<a class="btn hero-btn abs">Download Samples <svg width="26" height="10" viewBox="0 0 26 10"><path d="M0 5h23M19 1l4 4-4 4" stroke="#fff" stroke-width="1.6" fill="none"/></svg></a>

<section class="about abs"></section>
<h2 class="imagine heading abs">Imagine <span>we promote</span></h2>
<div class="copy copy1 abs">
  <p>being able to create exciting give away promotions that will boost your sales without ever having to worry about cost</p>
  <p><b>Blue Willow Promo Group, Inc.</b> provides high-perceived value promotional incentives to businesses that want to advertise an exciting Give Away that will instantly attract more customers from your existing advertising efforts.</p>
  <p>Your business can give away incentive certificates that are redeemable for luxury hotel &amp; resort stays with airfare included, <b>cruises, cash for gas, groceries, dining and even electronic goods.</b></p>
</div>
<div class="rule abs"></div>
<h2 class="how heading abs">How can we do it?</h2>
<div class="copy copy2 abs">
  <p>We help fill empty rooms for thousands of hotels and resorts in hundreds of destinations around the world as well as the major cruise lines. Hotels and resorts are rarely full so when we place someone in their empty rooms, they end up making it up when travelers spend money on room service, spa services, eat at their in-house restaurants, casino and take advantage of other amenities that drive revenue.</p>
  <p><b>We also help over 18,000 restaurants, electronic manufacturers, the major gas companies and top grocery chains in the U.S and Canada increase brand awareness as well as increase customer loyalty.</b></p>
</div>

<h3 class="why-title heading abs">Why Offer Incentives To Customers?</h3>
<div class="why-underline abs"></div>
<div class="why-axis abs"></div>
<div class="dot abs" style="left:875px;top:855px"></div>
<div class="dot abs" style="left:875px;top:1014px"></div>
<div class="dot abs" style="left:875px;top:1180px"></div>

<div class="benefit abs" style="left:697px;top:790px"><svg width="40" height="40" viewBox="0 0 40 40"><rect x="4" y="24" width="7" height="14" fill="#2f8fd6"/><rect x="14" y="18" width="7" height="20" fill="#2f8fd6"/><rect x="24" y="12" width="7" height="26" fill="#2f8fd6"/><path d="M4 18 18 8l6 4 12-9" stroke="#5bb04a" stroke-width="3" fill="none"/></svg>Increase Responses From Your Existing Ads</div>
<div class="benefit abs" style="left:890px;top:790px"><svg width="40" height="40" viewBox="0 0 40 40"><circle cx="15" cy="14" r="9" fill="none" stroke="#8a8f96" stroke-width="4"/><path d="M21 20l14 14" stroke="#c0392b" stroke-width="6" stroke-linecap="round"/></svg>#1 Sales Closing Tool - Gift w/Purchase</div>
<div class="benefit abs" style="left:697px;top:950px"><svg width="40" height="40" viewBox="0 0 40 40"><path d="M20 3l5 11 12 1-9 8 3 12-11-6-11 6 3-12-9-8 12-1z" fill="#f5b400"/></svg>Build Brand Awareness and Trust</div>
<div class="benefit abs" style="left:890px;top:950px"><svg width="40" height="40" viewBox="0 0 40 40"><circle cx="14" cy="11" r="6" fill="#3a8fd6"/><path d="M3 30q0-11 11-11t11 11z" fill="#3a8fd6"/><circle cx="27" cy="17" r="6" fill="#5bb04a"/><path d="M16 37q0-11 11-11t11 11z" fill="#5bb04a"/></svg>Insure The Sale Over Your Competition</div>
<div class="benefit abs" style="left:697px;top:1115px"><svg width="40" height="40" viewBox="0 0 40 40"><path d="M8 14h20v-6l8 9-8 9v-6H8z" fill="#3a8fd6"/><path d="M32 26H12v6l-8-9 8-9v6h20z" fill="#7fb9e6" transform="translate(0 4)"/></svg>Boost Repeat and Referral Business</div>
<div class="benefit abs" style="left:890px;top:1115px"><svg width="40" height="40" viewBox="0 0 40 40"><circle cx="20" cy="20" r="16" fill="#3a8fd6"/><text x="20" y="27" text-anchor="middle" font-family="Open Sans,sans-serif" font-weight="700" font-size="20" fill="#fff">$</text></svg>Improve Retention Rates</div>

<section class="lead abs"></section>
<div class="card form-card abs"></div>
<p class="form-title abs"><strong>Enter your info</strong>to be forward to our website for the all details and to recive sample in your email!</p>
<div class="label abs" style="left:193px;top:1553px">Full name*</div>
<div class="field abs" style="left:193px;top:1578px;width:180px">john doe</div>
<div class="label abs" style="left:383px;top:1553px">Phone*</div>
<div class="field abs" style="left:383px;top:1578px;width:180px">+55-1234567</div>
<div class="label abs" style="left:193px;top:1632px">Email*</div>
<div class="field abs" style="left:191px;top:1655px;width:374px">janedoe@mail.example</div>
<div class="mandatory abs">*mandatory field</div>
<a class="btn form-btn abs">Download Samples <svg width="12" height="22" viewBox="0 0 12 22"><path d="M6 0v19M2 15l4 4 4-4" stroke="#fff" stroke-width="1.6" fill="none"/></svg></a>

<div class="card testi-card abs"></div>
<h3 class="testi-title abs">Client testimonials</h3>
<div class="quote-mark abs">&ldquo;</div>
<p class="testi-text abs">I began using your incentives two years ago to boost lead generation efforts. I have experienced a 63% increase in lead captures. And, even more importantly, my sales have increased as well. The ability to offer unlimited certificates and not having to pay for each certificate I give away is perhaps the best feature of the program, but having the flexibility to email or print certificates for my customers is also wonderful. I even use your html banners to automate my promotions right on my website!</p>
<div class="testi-name abs">Dan R.</div>
<div class="testi-place abs">Cedarton, OH</div>

<h2 class="clients-title heading abs">OUR CLIENTS</h2>
<svg class="chev abs" style="left:22px" width="14" height="26" viewBox="0 0 14 26"><path d="M12 2 2 13l10 11" stroke="#9aa" stroke-width="2" fill="none"/></svg>
<div class="client-row abs">
  <div class="client">Northlane</div>
  <div class="client">Corvamart</div>
  <div class="client">Ridgeway Motors</div>
  <div class="client">Halden Trust</div>
  <div class="client">Clearpane Co.</div>
</div>
<svg class="chev abs" style="left:1162px" width="14" height="26" viewBox="0 0 14 26"><path d="M2 2l10 11L2 24" stroke="var(--blue)" stroke-width="2" fill="none"/></svg>

<footer class="site-footer abs"></footer>
<div class="brand abs" style="top:2326px"><span class="brand-mark" style="width:24px;height:24px"></span><span class="brand-name" style="font-size:16px">BLUE WILLOW PROMOS</span></div>
<p class="f-about abs">We've enrolled more than 13,000 businesses into our program who are responsible for distributing over 3+ million certificates to their customers and we have an A rating with the Trade Bureau.</p>
<div class="f-head abs" style="left:160px;top:2474px;font-size:13px">Follow us</div>
<div class="social abs" aria-label="Social links">
  <i style="background:#2d4a86"></i><i style="background:#2aa3d8"></i><i style="background:#1b6fa8"></i><i style="background:#d9443a"></i>
</div>

<div class="f-head abs" style="left:458px;top:2330px">Quick links</div>
<div class="f-bar abs" style="left:458px;top:2356px"></div>
<div class="f-links abs" style="left:460px;top:2375px">Home<br>Our Incentives<br>Samples<br>Affiliate<br>Testimonials<br>Faq<br>Contact Us<br>Terms &amp; Conditions<br>Privacy Policy</div>

<div class="f-head abs" style="left:594px;top:2330px">Contact details</div>
<div class="f-bar abs" style="left:594px;top:2356px"></div>
<div class="contact-row abs" style="left:592px;top:2380px">
  <svg width="16" height="20" viewBox="0 0 16 20"><path d="M8 19S2 11 2 7a6 6 0 0112 0c0 4-6 12-6 12z" fill="none" stroke="var(--orange)" stroke-width="1.6"/><circle cx="8" cy="7" r="2" fill="var(--orange)"/></svg>
  <div class="f-text" style="line-height:18px"><b>Blue Willow Promo<br>Group, Inc.</b><br><span style="display:block;margin-top:12px">410 Harbor Lane<br>Bayview CA 90000</span></div>
</div>
<div class="contact-row abs" style="left:592px;top:2484px">
  <svg width="16" height="18" viewBox="0 0 16 18"><path d="M3 1l3 4-2 2q2 4 6 6l2-2 4 3-2 3Q6 17 1 4z" fill="none" stroke="var(--blue)" stroke-width="1.5"/></svg>
  <div class="f-text" style="line-height:18px;font-weight:700">555-014-2287<br>1-800-555-0199</div>
</div>
<div class="contact-row abs" style="left:592px;top:2538px">
  <svg width="16" height="16" viewBox="0 0 16 16"><rect x="1" y="2" width="14" height="13" fill="none" stroke="var(--blue)" stroke-width="1.5"/><path d="M1 6h14M5 9h2M9 9h2M5 12h2" stroke="var(--blue)" stroke-width="1.5"/></svg>
  <div class="f-text" style="line-height:18px">Hours: Mon-Fri 7am - 4pm PST<br>Sat-Sun <b>CLOSED</b></div>
</div>

<div class="f-head abs" style="left:826px;top:2330px">Contact now</div>
<div class="f-bar abs" style="left:826px;top:2356px"></div>
<div class="f-input abs" style="left:826px;top:2382px">Your name</div>
<div class="f-input abs" style="left:826px;top:2434px">Your email</div>
<div class="f-input abs" style="left:826px;top:2486px;height:90px">Message</div>
<a class="btn submit abs">Submit</a>

<div class="copyright abs">© 2005-2017 Blue Willow Promo Group, Inc. - All Rights Reserved</div>

</body>
</html>
```